Brell Harbor Company Business Cards

Front and Back Business Card - logo and text setup - cool design. I need workable photoshop or illustrator files so I can setup each employee card with design that is created
Updates

Hi everyone, thank you for the great entries. Please no more white and blue cards - there are so many already - black and silver only now please. thanks!

Target Market(s)

Construction Industry - Facility Managers

Industry/Entity Type

Construction

Contact Information for Business Card

I really like contemporary simplistic looks - clean neat....not opposed to seeing some black backrounds

Requirements
Must have
• Logo/website address with design on front only - www.brellharbor-example.com (logo attached)
• Back:
• Name/Title/Company Address/Phone/email address
Nice to have
• Cool design
Should not have
• Nothing gimmicky like Fire or Water - since we are a Fire Protection company - it has all been done

```html
<!DOCTYPE html>
<html lang="en">
<head>
<meta charset="utf-8">
<title>Brell Harbor Company Business Cards</title>
<link href="https://fonts.googleapis.com/css2?family=Roboto:wght@400;500;700;900&display=swap" rel="stylesheet">
<style>
  :root {
    --backdrop: #1d1d1f;
    --card: #0c0c0d;
    --brand-blue: #2e4a8e;
    --brand-red: #ec4a2e;
    --band-light: #fbe3da;
    --text-light: #f2f2f2;
    --rule: #6a6a6a;
  }
  html, body {
    margin: 0;
    padding: 0;
    width: 1200px;
    height: 1200px;
    overflow: hidden;
    background: var(--backdrop);
    font-family: "Roboto", Arial, sans-serif;
  }
  .canvas {
    position: relative;
    width: 1200px;
    height: 1200px;
  }
  .card {
    position: absolute;
    left: 150px;
    width: 900px;
    height: 514px;
    background: var(--card);
    box-shadow: 0 18px 40px rgba(0,0,0,0.55);
    overflow: hidden;
  }
  .card--front { top: 62px; }
  .card--back { top: 622px; }

  .wordmark {
    margin: 0;
    font-weight: 900;
    color: var(--brand-blue);
    letter-spacing: -1px;
    display: flex;
    align-items: center;
    gap: 14px;
    white-space: nowrap;
  }
  .wordmark__square {
    display: inline-block;
    background: var(--brand-red);
  }

  /* Front */
  .card--front .wordmark {
    position: absolute;
    top: 188px;
    left: 0;
    right: 0;
    justify-content: center;
    font-size: 64px;
  }
  .card--front .wordmark__square { width: 38px; height: 38px; }
  .website {
    position: absolute;
    bottom: 78px;
    left: 0;
    right: 0;
    margin: 0;
    text-align: center;
    font-size: 20px;
    font-weight: 500;
    letter-spacing: 0.5px;
    color: var(--brand-blue);
  }
  .website__accent { color: var(--brand-red); }

  /* Back */
  .card--back .wordmark {
    position: absolute;
    top: 150px;
    left: 48px;
    font-size: 42px;
  }
  .card--back .wordmark__square { width: 26px; height: 26px; }
  .divider {
    position: absolute;
    left: 452px;
    top: 120px;
    width: 1px;
    height: 190px;
    background: var(--rule);
  }
  .contact {
    position: absolute;
    left: 486px;
    top: 130px;
    color: var(--text-light);
  }
  .contact__name {
    margin: 0;
    font-size: 30px;
    font-weight: 700;
    line-height: 1;
  }
  .contact__first { color: var(--brand-blue); }
  .contact__last { color: var(--brand-red); }
  .contact__title {
    margin: 4px 0 22px;
    font-size: 19px;
    color: var(--brand-red);
  }
  .contact__address {
    margin: 0 0 12px;
    font-style: normal;
    font-size: 20px;
    line-height: 1.3;
  }
  .contact__line {
    display: flex;
    align-items: center;
    gap: 14px;
    font-size: 20px;
    line-height: 1.6;
  }
  .contact__icon { width: 20px; height: 20px; flex: none; }
  .accent-band {
    position: absolute;
    left: 0;
    bottom: 42px;
    width: 900px;
    height: 16px;
    background: linear-gradient(90deg, var(--band-light) 0%, #f7a386 45%, var(--brand-red) 100%);
  }
</style>
</head>
<body>
<main class="canvas">

  <section class="card card--front" aria-label="Card front">
    <h1 class="wordmark"><span class="wordmark__square"></span>Brell Harbor</h1>
    <p class="website">www.<span class="website__accent">brellharbor-example.com</span></p>
  </section>

  <section class="card card--back" aria-label="Card back">
    <h2 class="wordmark"><span class="wordmark__square"></span>Brell Harbor</h2>
    <div class="divider"></div>
    <div class="contact">
      <p class="contact__name"><span class="contact__first">Marcus</span> <span class="contact__last">Delane</span></p>
      <p class="contact__title">President</p>
      <address class="contact__address">118 Linden Court NW, Suite 300<br>Alder Falls, MI 49000</address>
      <div class="contact__line">
        <svg class="contact__icon" viewBox="0 0 24 24" aria-hidden="true"><path fill="#ec4a2e" d="M6.6 10.8a15.1 15.1 0 0 0 6.6 6.6l2.2-2.2a1 1 0 0 1 1-.25 11.4 11.4 0 0 0 3.6.57 1 1 0 0 1 1 1V20a1 1 0 0 1-1 1A17 17 0 0 1 3 4a1 1 0 0 1 1-1h3.5a1 1 0 0 1 1 1c0 1.25.2 2.45.57 3.57a1 1 0 0 1-.25 1z"/></svg>
        <span>555.014.2280</span>
      </div>
      <div class="contact__line">
        <svg class="contact__icon" viewBox="0 0 24 24" aria-hidden="true"><rect x="2" y="5" width="20" height="14" fill="none" stroke="#ec4a2e" stroke-width="2"/><path d="M2 5l10 8 10-8M2 19l7-7M22 19l-7-7" fill="none" stroke="#ec4a2e" stroke-width="2"/></svg>
        <span>info@brellharbor-example.com</span>
      </div>
    </div>
    <div class="accent-band" role="img" aria-label="Decorative accent band fading from pale peach to red"></div>
  </section>

</main>
</body>
</html>
```